One page design needed for a veteran owned brewery

I need a one page web designed for a brewery that is veteran owned. We give back a portion of our proceeds to veteran based nonprofit groups. halvardbrewing.example It is word press based.

Industry/Entity Type

Craft Brewery

Number of Pages Required

1 page

```html
<!DOCTYPE html>
<html lang="en">
<head>
<meta charset="utf-8">
<title>Halvard Brewery</title>
<link href="https://fonts.googleapis.com/css2?family=Montserrat:wght@400;600;700&display=swap" rel="stylesheet">
<style>
  :root {
    --ink: #1c1c1c;
    --white: #ffffff;
    --hop-green: #6aa843;
    --header-grey: #7a7a7a;
    --body-text: #2a2a2a;
    --icon-grey: #8a8a8a;
  }
  * { margin: 0; padding: 0; box-sizing: border-box; }
  html, body { width: 1200px; height: 1110px; overflow: hidden; background: var(--white); }
  body { font-family: "Montserrat", sans-serif; position: relative; }

  .hero {
    position: absolute; left: 0; top: 0; width: 1200px; height: 602px;
    background:
      radial-gradient(ellipse 220px 260px at 660px 390px, #e08a1c 0%, #c46a10 45%, rgba(120,60,10,0) 100%),
      linear-gradient(90deg, #5a5a5a 0%, #1a1a1a 22%, #2a2a2a 45%, #3a3a3a 60%, #141414 80%, #2b2b2b 100%);
  }
  .hero-photo { position: absolute; inset: 0; }

  .site-header {
    position: absolute; left: 0; top: 0; width: 1200px; height: 86px;
    background: linear-gradient(90deg, #5c5c5c 0%, #8a8a8a 40%, #bdbdbd 60%, #9a9a9a 100%);
    display: flex; align-items: center; justify-content: space-between;
    padding: 0 86px;
  }
  .brand { display: flex; align-items: center; gap: 8px; }
  .brand-dot { width: 14px; height: 14px; border-radius: 50%; background: var(--ink); }
  .brand-name { font-weight: 700; font-size: 15px; color: var(--ink); letter-spacing: 0.5px; text-transform: uppercase; }
  .nav-link {
    font-size: 11px; font-weight: 400; color: var(--ink); text-transform: uppercase;
    display: flex; align-items: center; gap: 6px;
  }
  .nav-link::before, .nav-link::after {
    content: ""; width: 5px; height: 5px; border-radius: 50%; background: var(--ink);
  }

  .hero-copy { position: absolute; left: 0; top: 278px; width: 1200px; text-align: center; }
  .hero-title { font-weight: 700; font-size: 69px; line-height: 1; color: var(--white); letter-spacing: 0.5px; }
  .hero-title .accent { color: var(--hop-green); }
  .hero-tagline { margin-top: 30px; font-weight: 700; font-size: 20.5px; color: var(--white); letter-spacing: 0.2px; }

  .about { position: absolute; left: 0; top: 602px; width: 1200px; height: 508px; }
  .about-text { position: absolute; right: 658px; top: 126px; text-align: right; width: 420px; }
  .about-heading { font-weight: 600; font-size: 35px; color: var(--ink); line-height: 1; }
  .about-body { margin-top: 30px; font-size: 16px; line-height: 31px; color: var(--body-text); }
  .anchor-icon { position: absolute; left: 336px; top: 300px; }
  .about-image {
    position: absolute; left: 602px; top: 86px; width: 516px; height: 344px;
    background: linear-gradient(90deg, #6f6a62 0%, #2a2a2a 15%, #1d1d1d 60%, #b4202a 82%, #2f3d7a 100%);
  }
</style>
</head>
<body>
  <section class="hero">
    <div class="hero-photo" role="img" aria-label="Row of glasses of dark and amber craft beer with foamy heads"></div>
    <header class="site-header">
      <div class="brand">
        <span class="brand-dot"></span>
        <span class="brand-name">Halvard</span>
      </div>
      <a class="nav-link">Find out more</a>
    </header>
    <div class="hero-copy">
      <h1 class="hero-title">HALVARD <span class="accent">BREWERY</span></h1>
      <p class="hero-tagline">BREWING FOR VETERANS AND LOCAL HEROS</p>
    </div>
  </section>

  <section class="about">
    <div class="about-text">
      <h2 class="about-heading">Halvard Brewery</h2>
      <p class="about-body">We are a veteran owned and operated brewery.<br>Our goal is to donate a percentage of our proceeds<br>to veteran organizations and our local heroes.</p>
    </div>
    <svg class="anchor-icon" width="14" height="18" viewBox="0 0 14 18" aria-hidden="true">
      <circle cx="7" cy="2.5" r="1.8" fill="none" stroke="var(--icon-grey)" stroke-width="1.4"/>
      <line x1="7" y1="4.3" x2="7" y2="16" stroke="var(--icon-grey)" stroke-width="1.6"/>
      <line x1="4" y1="7" x2="10" y2="7" stroke="var(--icon-grey)" stroke-width="1.4"/>
      <path d="M1.5 10.5 Q2 16 7 16 Q12 16 12.5 10.5" fill="none" stroke="var(--icon-grey)" stroke-width="1.6"/>
    </svg>
    <div class="about-image" role="img" aria-label="Chalkboard sign reading thank you veterans in front of an American flag on weathered wood"></div>
  </section>
</body>
</html>
```